Need Letterhead Design & Matching Business Card

I have a logo that I love already. But the letterhead is less than appealing and boring. I'd like a design for my letterhead which I will match with business cards. Also, I'd like to have used fonts that are generally available, as my current letterhead uses a font named "SPACE" which nobody has unless they download it...so when a Word version is forwarded, it looks awful on the receiver's screed due to not having the font. That being said, modern is the look we like and are going for.

My business is "Halloran Brightmoor PC" - a law firm specializing in representing people who have suffered catastrophic injuries or death (plane, auto, train crashes etc.).

See attached letterhead, which has all of the pertinent information. My logo is also attached in various formats.

```html
<!DOCTYPE html>
<html lang="en">
<head>
<meta charset="utf-8">
<title>Halloran Brightmoor PC — Letterhead</title>
<link href="https://fonts.googleapis.com/css2?family=Josefin+Sans:wght@300;600&display=swap" rel="stylesheet">
<style>
  :root {
    --backdrop: #e6e7e9;
    --paper: #ffffff;
    --ink: #07080a;
    --reverse: #ffffff;
    --watermark: #ebe9ea;
  }
  * { margin: 0; padding: 0; box-sizing: border-box; }
  html, body {
    width: 933px;
    height: 1200px;
    overflow: hidden;
    background: var(--backdrop);
    font-family: "Josefin Sans", sans-serif;
  }
  .letterhead {
    position: absolute;
    left: 48px;
    top: 53px;
    width: 834px;
    height: 1081px;
    background: var(--paper);
  }
  .masthead {
    position: absolute;
    left: 0;
    top: 0;
    width: 834px;
    height: 174px;
    background: var(--ink);
    color: var(--reverse);
  }
  .brand-square {
    position: absolute;
    left: 42px;
    top: 38px;
    width: 98px;
    height: 98px;
    border: 5px solid var(--reverse);
  }
  .firm-name {
    position: absolute;
    left: 165px;
    top: 36px;
    font-weight: 300;
    font-size: 39px;
    line-height: 1;
    letter-spacing: 3px;
    white-space: nowrap;
  }
  .firm-name .suffix {
    font-weight: 600;
    font-size: 15px;
    letter-spacing: 1px;
    vertical-align: 16px;
    margin-left: 4px;
  }
  .contact {
    position: absolute;
    top: 95px;
    font-style: normal;
    font-weight: 600;
    font-size: 10px;
    line-height: 15px;
    letter-spacing: 1px;
    text-transform: uppercase;
    white-space: nowrap;
  }
  .contact-office { left: 283px; }
  .contact-reach { left: 565px; }
  .contact-divider {
    position: absolute;
    left: 552px;
    top: 96px;
    width: 1px;
    height: 44px;
    background: var(--reverse);
  }
  .watermark {
    position: absolute;
    left: 0;
    top: 560px;
    width: 834px;
    text-align: center;
    color: var(--watermark);
    font-weight: 600;
    font-size: 72px;
    line-height: 1.15;
    letter-spacing: 6px;
  }
</style>
</head>
<body>
  <main class="letterhead">
    <header class="masthead">
      <div class="brand-square" aria-hidden="true"></div>
      <h1 class="firm-name">HALLORAN BRIGHTMOOR<span class="suffix">PC</span></h1>
      <address class="contact contact-office">
        R. Damon Castell, Esq. | President<br>
        4410 Canyon Crest Dr. | Suite 1200<br>
        Lakeview Heights, CA 90418
      </address>
      <div class="contact-divider" aria-hidden="true"></div>
      <address class="contact contact-reach">
        damon@halloranbrightmoor.com<br>
        www.halloranbrightmoor.com<br>
        Tel: (855) 402-7718
      </address>
    </header>
    <div class="watermark" aria-hidden="true">HALLORAN<br>BRIGHTMOOR</div>
  </main>
</body>
</html>
```